Ledgers of the Realm - e-book cover

Summary
• The requirement is for a cover design for the e-book with the above title to be used when publishing the book on Brindle, Quince Readshelf’s, etc plus sales from our own website
Book details
• Since this will only be an e-book the cover should display well in the small size available to view e-books as a prospective purchase – see Brindle Pagebox examples
• The full book title is “Ledgers of the realm: from levy to ledger review”
• The brief description of the book is “How governments plan, raise, spend and then account for their use of citizens’ money in the 21st century”
• The authors are “Gordon Kettleby and Ronan Whitlow”
Key themes of the book
We accept that these themes may not all be represented in a cover design but they are included to emphasise our goals:
1. Governments raise money from and on behalf of citizens
2. Governments manage and use such public money for the benefit of citizens
3. Governments are accountable to citizens for such use of public money
4. Governments should enable accountability through transparent fiscal reporting
5. Governments have an obligation to ensure the sustainability of finance and service delivery for future generations
6. How better to achieve all of the above in the 21st century

Target Market(s)

Politicians, officials and students from governments across the world together with their advisers including accountants and economists

Font styles to use
Serif
Sans Serif

Colors
33a6d7
3176b5

Requirements
Must have
• See project brief uploaded file
Nice to have
• See project brief in uploaded file
Should not have

```html
<!DOCTYPE html>
<html lang="en">
<head>
<meta charset="utf-8">
<title>Ledgers of the Realm – e-book cover</title>
<link rel="stylesheet" href="https://fonts.googleapis.com/css2?family=Bebas+Neue&family=Fira+Sans+Extra+Condensed:ital,wght@1,500&family=Lato:wght@400&display=swap">
<style>
  :root {
    --page-bg: #f1f1f1;
    --cover-blue: #1776a3;
    --title-white: #ffffff;
    --accent-yellow: #fcc419;
    --ink-dark: #222222;
    --road-dark: #333335;
    --road-mid: #2b5f82;
  }
  html, body {
    margin: 0;
    width: 1200px;
    height: 1200px;
    overflow: hidden;
    background: var(--page-bg);
  }
  .cover {
    position: absolute;
    left: 254px;
    top: 82px;
    width: 691px;
    height: 1035px;
    background: var(--cover-blue);
    overflow: hidden;
  }
  .title {
    position: absolute;
    left: 0;
    right: 0;
    top: 34px;
    margin: 0;
    text-align: center;
    font-family: "Bebas Neue", "Oswald", sans-serif;
    font-weight: 400;
    color: var(--title-white);
    line-height: 0.84;
    font-size: 150px;
    letter-spacing: 1px;
  }
  .title .title-small { font-size: 112px; }
  .subtitle {
    position: absolute;
    left: 0;
    right: 0;
    top: 298px;
    margin: 0;
    text-align: center;
    font-family: "Bebas Neue", "Oswald", sans-serif;
    font-weight: 400;
    font-size: 62px;
    letter-spacing: 2px;
    color: var(--accent-yellow);
  }
  .cover-illustration {
    position: absolute;
    left: 34px;
    top: 382px;
    width: 640px;
    height: 380px;
    border-radius: 40px 120px 40px 20px;
    background: radial-gradient(ellipse at 50% 45%, var(--road-dark) 0%, #3a3d42 45%, var(--road-mid) 100%);
  }
  .tagline-band {
    position: absolute;
    left: 175px;
    top: 778px;
    width: 516px;
    height: 141px;
    margin: 0;
    background: var(--accent-yellow);
    box-sizing: border-box;
    padding: 10px 52px 0 0;
    text-align: right;
    white-space: nowrap;
    font-family: "Fira Sans Extra Condensed", "Arial Narrow", sans-serif;
    font-style: italic;
    font-weight: 500;
    font-size: 35px;
    line-height: 45px;
    color: var(--ink-dark);
  }
  .tagline-band sup {
    font-size: 0.62em;
    line-height: 0;
    vertical-align: 0.7em;
  }
  .authors {
    position: absolute;
    left: 0;
    right: 0;
    top: 956px;
    margin: 0;
    text-align: center;
    font-family: "Lato", sans-serif;
    font-variant: small-caps;
    font-size: 38px;
    letter-spacing: 1px;
    color: var(--title-white);
  }
</style>
</head>
<body>
  <div class="cover">
    <h1 class="title">Ledgers <span class="title-small">of</span><br>The Realm:</h1>
    <p class="subtitle">From Levy to Ledger Review</p>
    <div class="cover-illustration" role="img" aria-label="Winding road shaped like a currency sign with road signs for transportation, science, culture, defence, healthcare and education, an under-construction barrier, traffic cones and a speed-limit sign"></div>
    <p class="tagline-band">How Governments Plan, Raise,<br>Spend &amp; then Account for their use<br>of Citizens’ Money in the 21<sup>st</sup> Century</p>
    <p class="authors">Gordon Kettleby &amp; Ronan Whitlow</p>
  </div>
</body>
</html>
```